Kitchen manufaturer business card/logo design

I am a small kitchen manufacturing company that makes and installs all sorts of cabinetry.

The colours im looking to incorporate in the card are light/baby blue, white and black.

Incorporate 5 stars to show quality workmanship and product.

Looking for a modern classy design.
Updates

Hey guys, New idea. The logo should be made using HK in the most modern way possible as well as the full company name below it. Thanks.

Target Market(s)

Anyone with a home thats looking for a new cabinetry of any sort.

Industry/Entity Type

Business

Contact Information for Business Card

Harbor Kitchens
Ted Lowther
PH 0491 358 902
Email- harborkitchens@mailvane.example
ABN- 83 507 962 318
-Kitchens
-Vanities
-Laundries
-Media Units
-Studies
-Wardrobes
-3D Computer Designs

Requirements
Must have

• The front of the card must only have the company name.
The different types of cabinetry I do must be on the back of the card in point form but instead of using points use stars.
Nice to have
• Just think classy and quality

```html
<!DOCTYPE html>
<html lang="en">
<head>
<meta charset="utf-8">
<title>Ted Lowther – Business Card</title>
<link rel="stylesheet" href="https://fonts.googleapis.com/css2?family=Pinyon+Script&family=Roboto:wght@300;400&display=swap">
<style>
  :root {
    --bg-light: #727272;
    --bg-dark: #050505;
    --band-light: #3cc0ee;
    --band-main: #1ea7db;
    --band-deep: #0b86b8;
    --white: #ffffff;
    --ink: #111111;
    --star-light: #e6e6e6;
    --star-dark: #6a6a6a;
  }
  html, body {
    margin: 0;
    padding: 0;
    overflow: hidden;
    background: #ffffff;
  }
  .card {
    position: relative;
    width: 1200px;
    height: 726px;
    overflow: hidden;
    background: linear-gradient(100deg, var(--bg-light) 0%, #4a4a4a 35%, #1c1c1c 65%, var(--bg-dark) 100%);
    font-family: "Roboto", Arial, sans-serif;
    color: var(--white);
  }
  .services {
    position: absolute;
    left: 56px;
    top: 48px;
    margin: 0;
    padding: 0;
    list-style: none;
    font-size: 50px;
    font-weight: 400;
    line-height: 68px;
    width: 1120px;
    letter-spacing: -0.5px;
  }
  .services li {
    display: inline-block;
    margin-right: 10px;
    white-space: nowrap;
  }
  .services .line-break {
    display: block;
    height: 0;
    margin: 0;
  }
  .star {
    width: 30px;
    height: 30px;
    vertical-align: 2px;
    margin-right: 2px;
  }
  .band {
    position: absolute;
    left: 0;
    top: 190px;
    width: 1200px;
    height: 400px;
  }
  .name {
    position: absolute;
    left: 0;
    width: 1200px;
    top: 255px;
    margin: 0;
    text-align: center;
    font-family: "Pinyon Script", cursive;
    font-weight: 400;
    font-size: 150px;
    line-height: 1;
    color: var(--white);
    text-shadow: 3px 4px 6px rgba(0,0,0,0.55);
  }
  .abn {
    position: absolute;
    left: 0;
    width: 1200px;
    top: 424px;
    margin: 0;
    text-align: center;
    font-weight: 300;
    font-size: 46px;
    color: var(--ink);
    letter-spacing: 0.5px;
  }
  .contact {
    position: absolute;
    top: 612px;
    left: 44px;
    display: flex;
    align-items: center;
    font-size: 46px;
    font-weight: 300;
    text-shadow: 2px 2px 4px rgba(0,0,0,0.5);
  }
  .contact-item {
    display: flex;
    align-items: center;
    margin-right: 48px;
    white-space: nowrap;
  }
  .contact-icon {
    width: 42px;
    height: 42px;
    margin-right: 8px;
  }
</style>
</head>
<body>
<main class="card">
  <svg width="0" height="0" style="position:absolute">
    <defs>
      <linearGradient id="star-fill" x1="0" y1="0" x2="1" y2="1">
        <stop offset="0" stop-color="var(--star-light)"/>
        <stop offset="1" stop-color="var(--star-dark)"/>
      </linearGradient>
      <symbol id="star" viewBox="0 0 24 24">
        <path d="M12 1.5l3.1 6.9 7.4.7-5.6 5 1.7 7.4L12 17.6l-6.6 3.9 1.7-7.4-5.6-5 7.4-.7z" fill="url(#star-fill)" stroke="#3a3a3a" stroke-width="0.6"/>
      </symbol>
    </defs>
  </svg>

  <ul class="services">
    <li><svg class="star"><use href="#star"/></svg>Kitchens</li>
    <li><svg class="star"><use href="#star"/></svg>Vanities</li>
    <li><svg class="star"><use href="#star"/></svg>Laundries</li>
    <li><svg class="star"><use href="#star"/></svg>Media Units</li>
    <li class="line-break"></li>
    <li><svg class="star"><use href="#star"/></svg>Studies</li>
    <li><svg class="star"><use href="#star"/></svg>Wardrobes</li>
    <li><svg class="star"><use href="#star"/></svg>3D Computer Designs</li>
  </ul>

  <svg class="band" viewBox="0 0 1200 400" aria-hidden="true">
    <defs>
      <linearGradient id="band-fill" x1="0" y1="0" x2="0" y2="1">
        <stop offset="0" stop-color="var(--band-deep)"/>
        <stop offset="0.15" stop-color="var(--band-main)"/>
        <stop offset="0.55" stop-color="var(--band-light)"/>
        <stop offset="0.9" stop-color="var(--band-main)"/>
        <stop offset="1" stop-color="var(--band-deep)"/>
      </linearGradient>
      <filter id="band-shadow" x="-5%" y="-10%" width="110%" height="130%">
        <feDropShadow dx="0" dy="6" stdDeviation="8" flood-color="#000" flood-opacity="0.5"/>
      </filter>
    </defs>
    <path d="M0 18 C 380 22 900 28 1140 72 C 1198 86 1200 250 1150 312 C 1000 368 500 372 0 340 Z"
          fill="url(#band-fill)" filter="url(#band-shadow)"/>
  </svg>

  <h1 class="name">Ted Lowther</h1>
  <p class="abn">ABN- 83 507 962 318</p>

  <div class="contact">
    <span class="contact-item">
      <svg class="contact-icon" viewBox="0 0 24 24" aria-hidden="true">
        <path d="M6.6 2.5c.6-.3 1.3-.1 1.6.5l1.9 3.6c.3.6.2 1.2-.3 1.6L8.3 9.3c1 2.4 3 4.5 5.4 5.6l1.2-1.5c.4-.5 1.1-.6 1.6-.3l3.6 1.9c.6.3.8 1 .5 1.6l-1.1 2.4c-.4.8-1.2 1.3-2.1 1.2C9.6 19.6 4.2 14.2 3.6 6.4c-.1-.9.4-1.7 1.2-2.1z" fill="#ffffff"/>
      </svg>
      0491 358 902
    </span>
    <span class="contact-item">
      <svg class="contact-icon" viewBox="0 0 24 24" aria-hidden="true">
        <path d="M3 9.5L12 3l9 6.5V20H3z M3 9.5l9 6.5 9-6.5 M3 20l6.5-6 M21 20l-6.5-6" fill="none" stroke="#ffffff" stroke-width="1.4" stroke-linejoin="round"/>
      </svg>
      harborkitchens@mailvane.example
    </span>
  </div>
</main>
</body>
</html>
```